Women's Online Clothing Boutique Needs Business Cards

I already have a logo that I would like to use. Some of the things that interest me is black business cards, foil embossed logo, glossy embossed logo, leopard print, no yellow font, rounded edges. I even like just a large logo on the front side with all of my information on the back side.

Contact Information for Business Card

https://silverheron.shopvenlo.com/
https://www.pagelink.net/thesilverheronboutique/
https://www.picfeed.net/thesilverheronboutique/
silverheronboutique@mailora.net

Requirements
Must have
• My Logo
Nice to have
• Leopard Print
Should not have
• No Yellow Font

```html
<!DOCTYPE html>
<html lang="en">
<head>
<meta charset="utf-8">
<title>The Silver Heron Boutique – Business Cards</title>
<link rel="stylesheet" href="https://fonts.googleapis.com/css2?family=Quicksand:wght@500;600&display=swap">
<style>
  :root {
    --backdrop: #ecebea;
    --card: #262827;
    --gold: #c9a13a;
    --gold-deep: #8a6a1f;
    --ink-light: #f2f2f2;
  }
  * { margin: 0; padding: 0; box-sizing: border-box; }
  html, body { width: 1200px; height: 923px; overflow: hidden; }
  body {
    background: var(--backdrop);
    font-family: "Quicksand", sans-serif;
    position: relative;
  }
  .card {
    position: absolute;
    top: 152px;
    width: 355px;
    height: 620px;
    background: var(--card);
    border-radius: 18px;
  }
  .card--front { left: 208px; }
  .card--back { left: 638px; }

  .print-area {
    position: absolute;
    left: 20px;
    top: 19px;
    width: 315px;
    height: 434px;
    background: radial-gradient(ellipse at 85% 10%, var(--gold) 0%, var(--gold-deep) 45%, #3a3222 100%);
    border-radius: 2px;
  }

  .brand-name {
    position: absolute;
    left: 0;
    width: 100%;
    text-align: center;
    color: var(--gold);
    font-weight: 600;
    font-size: 30px;
    line-height: 1.2;
  }
  .card--front .brand-name { top: 498px; }
  .card--back .brand-name { top: 212px; }

  .contact-list {
    position: absolute;
    left: 0;
    top: 351px;
    width: 100%;
    list-style: none;
    text-align: center;
  }
  .contact-item {
    height: 56.5px;
    display: flex;
    flex-direction: column;
    align-items: center;
  }
  .contact-icon {
    width: 20px;
    height: 20px;
    display: block;
  }
  .contact-text {
    margin-top: 7px;
    color: var(--ink-light);
    font-size: 17px;
    font-weight: 500;
    letter-spacing: 0.1px;
    white-space: nowrap;
  }
  .base-rule {
    position: absolute;
    left: 23px;
    top: 594px;
    width: 310px;
    height: 2px;
    background: var(--gold);
  }
</style>
</head>
<body>
  <section class="card card--front">
    <div class="print-area" role="img" aria-label="Gold foil animal-spot print pattern"></div>
    <p class="brand-name">The Silver Heron<br>Boutique</p>
  </section>

  <section class="card card--back">
    <p class="brand-name">The Silver Heron<br>Boutique</p>
    <ul class="contact-list">
      <li class="contact-item">
        <svg class="contact-icon" viewBox="0 0 20 20" aria-hidden="true">
          <circle cx="10" cy="10" r="8.5" fill="none" stroke="var(--gold)" stroke-width="2"/>
          <ellipse cx="10" cy="10" rx="3.5" ry="8.5" fill="none" stroke="var(--gold)" stroke-width="1.5"/>
          <line x1="1.5" y1="10" x2="18.5" y2="10" stroke="var(--gold)" stroke-width="1.5"/>
        </svg>
        <span class="contact-text">www.silverheron.shopvenlo.com</span>
      </li>
      <li class="contact-item">
        <svg class="contact-icon" viewBox="0 0 20 20" aria-hidden="true">
          <rect x="1" y="4" width="18" height="13" rx="1.5" fill="var(--gold)"/>
          <polyline points="1.5,5 10,11.5 18.5,5" fill="none" stroke="var(--card)" stroke-width="1.5"/>
        </svg>
        <span class="contact-text">silverheronboutique@mailora.net</span>
      </li>
      <li class="contact-item">
        <svg class="contact-icon" viewBox="0 0 20 20" aria-hidden="true">
          <rect x="2" y="2" width="16" height="16" rx="3" fill="var(--gold)"/>
        </svg>
        <span class="contact-text">thesilverheronboutique</span>
      </li>
      <li class="contact-item">
        <svg class="contact-icon" viewBox="0 0 20 20" aria-hidden="true">
          <circle cx="10" cy="10" r="8.5" fill="var(--gold)"/>
        </svg>
        <span class="contact-text">thesilverheronboutique</span>
      </li>
    </ul>
    <div class="base-rule"></div>
  </section>
</body>
</html>
```